CD Cover Design Project

Although I posted a picture as a possible idea, an idea from scratch is mostly what I am looking for. Definitely listen to the song before making the design. The link is posted right here in the project overview.
I need a CD cover for my latest single. This artwork will go up on Sonvia, zelbrook, etc with the song. Please listen to the song and then creat the artwork. Here is a link to the song:
http://wavetrove.example/doriankeithvaldemar/under-amber-skies
The design needs my name, Dorian Keith Valdemar and it needs the song title, Under Amber Skies.
It needs to be a perfect square.
1600 by 1600
Resolution 300 DPI
Contact me at dorian@dorian-keith.example or (555) 014-2937

```html
<!DOCTYPE html>
<html lang="en">
<head>
<meta charset="utf-8">
<title>Dorian Keith Valdemar – Under Amber Skies</title>
<link rel="stylesheet" href="https://fonts.googleapis.com/css2?family=Permanent+Marker&family=Kalam:wght@700&display=swap">
<style>
  :root {
    --parchment-light: #e2b27a;
    --parchment-mid: #c98a4c;
    --parchment-dark: #8a4a1e;
    --ink: #111111;
    --frame: #f7f5ef;
    --frame-back: #ecebe5;
    --heart: #e8321f;
    --heart-dark: #c11f10;
    --clip: #7a7a7a;
  }
  html, body {
    margin: 0;
    padding: 0;
    overflow: hidden;
    background: #ffffff;
  }
  .cover {
    position: relative;
    width: 1200px;
    height: 1200px;
    overflow: hidden;
  }
  .cover__backdrop {
    position: absolute;
    inset: 0;
    background:
      radial-gradient(ellipse at 50% 45%, var(--parchment-light) 0%, var(--parchment-mid) 55%, var(--parchment-dark) 100%);
  }
  .cover__title {
    position: absolute;
    top: 18px;
    left: 0;
    width: 100%;
    margin: 0;
    text-align: center;
    font-family: "Permanent Marker", "Kalam", cursive;
    font-weight: 400;
    color: var(--ink);
    line-height: 1.2;
  }
  .cover__artist, .cover__song {
    display: block;
    font-size: 76px;
  }
  .polaroid {
    position: absolute;
  }
  .polaroid__back {
    position: absolute;
    background: var(--frame-back);
    box-shadow: 0 2px 6px rgba(0,0,0,0.35);
  }
  .polaroid__card {
    position: absolute;
    inset: 0;
    background: var(--frame);
    box-shadow: 0 4px 10px rgba(0,0,0,0.4);
  }
  .polaroid__photo {
    position: absolute;
  }
  .polaroid__caption {
    position: absolute;
    font-family: "Kalam", "Permanent Marker", cursive;
    font-weight: 700;
    font-size: 40px;
    color: var(--ink);
    white-space: nowrap;
  }
  .polaroid__clip {
    position: absolute;
    width: 10px;
    height: 26px;
    border: 3px solid var(--clip);
    border-radius: 6px;
    border-bottom: none;
  }

  /* clouds */
  .polaroid--clouds { left: 192px; top: 248px; width: 366px; height: 388px; }
  .polaroid--clouds .polaroid__photo {
    left: 24px; top: 28px; width: 318px; height: 286px;
    background: linear-gradient(180deg, #1f3fb0 0%, #5e86d8 30%, #d7e2f2 48%, #6fc23a 58%, #3f9a1e 100%);
  }
  .polaroid--clouds .polaroid__caption { left: 212px; top: 320px; }

  /* grass */
  .polaroid--grass { left: 604px; top: 282px; width: 370px; height: 350px; transform: rotate(4deg); }
  .polaroid--grass .polaroid__photo {
    left: 16px; top: 16px; width: 338px; height: 318px;
    background: linear-gradient(160deg, #1f4a0c 0%, #4f9a1c 45%, #8fd13a 70%, #2c6610 100%);
  }

  /* bench */
  .polaroid--bench { left: 222px; top: 666px; width: 368px; height: 404px; transform: rotate(-2deg); }
  .polaroid--bench .polaroid__photo {
    left: 24px; top: 26px; width: 322px; height: 304px;
    background: linear-gradient(180deg, #c8a46a 0%, #8c6a34 40%, #a8621c 70%, #6a3610 100%);
  }
  .polaroid--bench .polaroid__caption { left: 18px; top: 336px; font-size: 38px; }

  /* me and her */
  .polaroid--couple { left: 634px; top: 628px; width: 388px; height: 400px; transform: rotate(3deg); }
  .polaroid--couple .polaroid__photo {
    left: 20px; top: 28px; width: 340px; height: 292px;
    background: linear-gradient(180deg, #0d3b4a 0%, #2a7a8a 45%, #6ab0b8 62%, #e8a23a 74%, #101010 80%, #050505 100%);
  }
  .polaroid--couple .polaroid__caption { left: 92px; top: 328px; }

  .heart {
    position: absolute;
    left: 522px;
    top: 566px;
    width: 216px;
    height: 230px;
    transform: rotate(-4deg);
  }
</style>
</head>
<body>
<main class="cover">
  <div class="cover__backdrop" role="img" aria-label="Aged cracked parchment texture in warm amber tones"></div>

  <h1 class="cover__title">
    <span class="cover__artist">Dorian Keith Valdemar</span>
    <span class="cover__song">Under Amber Skies</span>
  </h1>

  <figure class="polaroid polaroid--clouds" style="margin:0">
    <div class="polaroid__back" style="left:24px; top:20px; width:356px; height:392px;"></div>
    <div class="polaroid__card">
      <div class="polaroid__photo" role="img" aria-label="Photo of white clouds over a green rolling hill"></div>
      <span class="polaroid__clip" style="right:40px; top:-14px;"></span>
      <figcaption class="polaroid__caption">clouds</figcaption>
    </div>
  </figure>

  <figure class="polaroid polaroid--grass" style="margin:0; transform: rotate(4deg);">
    <div class="polaroid__back" style="left:16px; top:14px; width:362px; height:346px;"></div>
    <div class="polaroid__card">
      <div class="polaroid__photo" role="img" aria-label="Close-up photo of grass blades with dew drops"></div>
      <span class="polaroid__clip" style="right:40px; top:-14px;"></span>
    </div>
  </figure>

  <figure class="polaroid polaroid--bench" style="margin:0; transform: rotate(-2deg);">
    <div class="polaroid__back" style="left:22px; top:22px; width:360px; height:404px;"></div>
    <div class="polaroid__card">
      <div class="polaroid__photo" role="img" aria-label="Photo of a park bench among autumn leaves"></div>
      <span class="polaroid__clip" style="right:40px; top:-14px;"></span>
      <figcaption class="polaroid__caption">Bench where we met</figcaption>
    </div>
  </figure>

  <figure class="polaroid polaroid--couple" style="margin:0; transform: rotate(3deg);">
    <div class="polaroid__back" style="left:18px; top:22px; width:380px; height:400px;"></div>
    <div class="polaroid__card">
      <div class="polaroid__photo" role="img" aria-label="Silhouette photo of a couple and a tree at sunset"></div>
      <span class="polaroid__clip" style="right:44px; top:-14px;"></span>
      <figcaption class="polaroid__caption">Me and Her</figcaption>
    </div>
  </figure>

  <svg class="heart" viewBox="0 0 200 210" aria-hidden="true">
    <path d="M100 200 C70 165 8 130 6 72 C4 30 36 6 66 8 C86 10 98 24 100 40 C104 22 118 6 142 6 C172 6 196 32 194 70 C190 128 130 162 100 200 Z"
          fill="var(--heart)" stroke="var(--heart-dark)" stroke-width="3"/>
  </svg>
</main>
</body>
</html>
```